" Minha empresa presta serviçoes de estética para gordura localizada, celulite, flacidez, rejuvenescimento, botox, preenchimento, redução de Estrias. Será uma marca licenciada para pessoas que queiram meus protocolos de atendimento. "

```html
<!DOCTYPE html>
<html lang="pt-BR">
<head>
<meta charset="utf-8">
<title>Assinatura de e-mail</title>
<link rel="stylesheet" href="https://fonts.googleapis.com/css2?family=Cinzel:wght@500&family=Open+Sans:wght@400;600&display=swap">
<style>
  :root {
    --page-bg: #ecebe8;
    --card-bg: #ffffff;
    --card-fade: #f1f0ee;
    --gold: #b8893f;
    --ink: #1f1f1f;
    --ink-soft: #3a3a3a;
    --bar: #111111;
  }
  html, body {
    margin: 0;
    width: 1200px;
    height: 1200px;
    overflow: hidden;
    background: var(--page-bg);
  }
  .canvas {
    width: 1200px;
    height: 1200px;
    display: flex;
    align-items: center;
    justify-content: center;
  }
  .signature {
    width: 1040px;
    background: var(--card-bg);
    box-shadow: 0 2px 12px rgba(0,0,0,0.06);
  }
  .signature__body {
    position: relative;
    height: 224px;
    display: flex;
    align-items: center;
    padding: 0 40px 0 48px;
    background: linear-gradient(90deg, var(--card-bg) 0%, var(--card-bg) 30%, var(--card-fade) 52%, var(--card-bg) 78%);
  }
  .brand {
    display: flex;
    align-items: center;
    gap: 14px;
    width: 390px;
  }
  .brand__dot {
    width: 18px;
    height: 18px;
    border-radius: 50%;
    background: var(--gold);
  }
  .brand__name {
    font-family: "Cinzel", serif;
    font-weight: 500;
    font-size: 40px;
    letter-spacing: 1px;
    color: var(--ink);
    margin-top: 40px;
  }
  .person {
    flex: 1;
    align-self: flex-end;
    padding-bottom: 44px;
    padding-left: 30px;
  }
  .person__name {
    font-family: "Open Sans", sans-serif;
    font-weight: 400;
    font-size: 22px;
    color: var(--gold);
    letter-spacing: 0.5px;
    border-top: 2px solid var(--gold);
    display: inline-block;
    padding-top: 6px;
  }
  .person__role {
    font-family: "Open Sans", sans-serif;
    font-size: 15px;
    color: var(--ink-soft);
    margin-top: 2px;
  }
  .contacts {
    list-style: none;
    margin: 0;
    padding: 0;
    display: flex;
    flex-direction: column;
    gap: 12px;
    align-items: flex-end;
  }
  .contacts__item {
    display: flex;
    align-items: center;
    gap: 14px;
    font-family: "Open Sans", sans-serif;
    font-size: 19px;
    color: var(--ink);
  }
  .contacts__icon {
    width: 22px;
    height: 22px;
    flex: none;
  }
  .signature__bar {
    height: 14px;
    background: var(--bar);
  }
</style>
</head>
<body>
<main class="canvas">
  <section class="signature">
    <div class="signature__body">
      <div class="brand">
        <span class="brand__dot"></span>
        <span class="brand__name">Mirela Antunes</span>
      </div>
      <div class="person">
        <div class="person__name">NOME SOBRENOME</div>
        <div class="person__role">CARGO/FUNÇÃO</div>
      </div>
      <ul class="contacts">
        <li class="contacts__item">
          <span>www.site.com.br</span>
          <svg class="contacts__icon" viewBox="0 0 24 24" fill="none" stroke="var(--gold)" stroke-width="2">
            <circle cx="12" cy="12" r="9"/>
            <ellipse cx="12" cy="12" rx="4" ry="9"/>
            <line x1="3" y1="12" x2="21" y2="12"/>
          </svg>
        </li>
        <li class="contacts__item">
          <span>99 99999-9999</span>
          <svg class="contacts__icon" viewBox="0 0 24 24">
            <circle cx="12" cy="12" r="9" fill="none" stroke="var(--gold)" stroke-width="2"/>
          </svg>
        </li>
        <li class="contacts__item">
          <span>99 9999-9999</span>
          <svg class="contacts__icon" viewBox="0 0 24 24" fill="none" stroke="var(--gold)" stroke-width="2">
            <rect x="7" y="2.5" width="10" height="19" rx="2"/>
            <line x1="11" y1="18" x2="13" y2="18"/>
          </svg>
        </li>
        <li class="contacts__item">
          <span>Rua do Projeto, 999</span>
          <svg class="contacts__icon" viewBox="0 0 24 24">
            <path d="M12 2a7 7 0 0 0-7 7c0 5 7 13 7 13s7-8 7-13a7 7 0 0 0-7-7z" fill="var(--gold)"/>
            <circle cx="12" cy="9" r="2.6" fill="var(--card-bg)"/>
          </svg>
        </li>
      </ul>
    </div>
    <div class="signature__bar"></div>
  </section>
</main>
</body>
</html>
```